Pebble Smiles Business Card

I need a business card designed for a dentist who works exclusively with children.
We prefer designs that are out of ordiary that is fun and interesting to kids.

there is no logo since this is a dentists office. The name of the doctor is "Tavro Kine" if you want to get creative with that.

Target Market(s)

Kids

Industry/Entity Type

Business

Contact Information for Business Card

Anythings that is creative

Colors

Designer to choose colors to be used in the design.

```html
<!DOCTYPE html>
<html lang="en">
<head>
<meta charset="utf-8">
<title>Pebble Smiles Business Card</title>
<link href="https://fonts.googleapis.com/css2?family=Open+Sans:wght@400;600;700&family=Questrial&display=swap" rel="stylesheet">
<style>
  :root {
    --stage: #000000;
    --card-white: #ffffff;
    --brand-blue: #1d7fc6;
    --brand-green: #8cc63f;
    --wordmark-grey: #7d7d7d;
    --text-dark: #333333;
    --back-blue: #21a9df;
    --back-green: #8dc85a;
  }
  * { margin: 0; padding: 0; box-sizing: border-box; }
  html, body {
    width: 1200px; height: 900px; overflow: hidden;
    background: var(--stage);
  }
  .canvas { position: relative; width: 1200px; height: 900px; }
  .card {
    position: absolute; top: 184px; width: 302px; height: 491px;
    border-radius: 14px; overflow: hidden;
  }
  .card--front { left: 299px; background: var(--card-white); }
  .card--back {
    left: 645px; width: 305px;
    background: radial-gradient(circle at 45% 42%, var(--back-blue) 0%, #3fb3b8 45%, var(--back-green) 90%);
  }
  .brand {
    position: absolute; left: 0; right: 0;
    display: flex; align-items: center; justify-content: center; gap: 10px;
    font-family: "Questrial", "Century Gothic", sans-serif;
    font-size: 29px; letter-spacing: 0.2px; white-space: nowrap;
  }
  .brand__dot { width: 18px; height: 18px; border-radius: 50%; }
  .card--front .brand { top: 173px; color: var(--wordmark-grey); }
  .card--front .brand__dot { background: var(--brand-green); }
  .card--back .brand { top: 282px; color: #ffffff; }
  .card--back .brand__dot { background: #ffffff; }

  .person {
    position: absolute; left: 31px; top: 250px;
    font-family: "Open Sans", sans-serif;
  }
  .person__name {
    color: var(--brand-blue); font-weight: 600; font-size: 24px;
    line-height: 30px; text-transform: uppercase; letter-spacing: 0.3px;
  }
  .person__role { color: var(--text-dark); font-size: 14px; line-height: 18px; text-transform: uppercase; }

  .contacts {
    position: absolute; left: 31px; top: 311px; list-style: none;
    font-family: "Open Sans", sans-serif; font-size: 15px; color: var(--text-dark);
  }
  .contacts li { display: flex; align-items: center; gap: 7px; height: 22px; }
  .contacts svg { width: 14px; height: 14px; flex: none; }

  .address {
    position: absolute; left: 34px; top: 412px;
    font-family: "Open Sans", sans-serif; font-size: 13px; line-height: 17px;
    color: var(--text-dark); font-style: normal;
  }
</style>
</head>
<body>
<main class="canvas">
  <section class="card card--front">
    <div class="brand"><span class="brand__dot"></span>Pebble Smiles</div>

    <div class="person">
      <div class="person__name">Tavro Kine</div>
      <div class="person__role">Director</div>
    </div>

    <ul class="contacts">
      <li>
        <svg viewBox="0 0 14 14"><circle cx="7" cy="7" r="7" fill="#1d7fc6"/><path d="M4 5.5c0-1 .8-1.5 3-1.5s3 .5 3 1.5v.6H8.6v-.7H5.4v.7H4zM4.5 7h5l.5 3H4z" fill="#fff"/></svg>
        403- 555-0142
      </li>
      <li>
        <svg viewBox="0 0 14 14"><circle cx="7" cy="7" r="7" fill="#1d7fc6"/><rect x="5" y="3.3" width="4" height="7.4" rx="0.8" fill="none" stroke="#fff" stroke-width="1"/></svg>
        403- 555-0187
      </li>
      <li>
        <svg viewBox="0 0 14 14"><circle cx="7" cy="7" r="7" fill="#1d7fc6"/><rect x="3.8" y="4.6" width="6.4" height="4.8" fill="#fff"/><path d="M3.8 4.6 7 7.3l3.2-2.7" fill="none" stroke="#1d7fc6" stroke-width="0.8"/></svg>
        hello@pebblesmiles.com
      </li>
      <li>
        <svg viewBox="0 0 14 14"><circle cx="7" cy="7" r="7" fill="#1d7fc6"/><circle cx="7" cy="7" r="3.4" fill="none" stroke="#fff" stroke-width="1"/><path d="M3.6 7h6.8M7 3.6c-1.6 2-1.6 4.8 0 6.8M7 3.6c1.6 2 1.6 4.8 0 6.8" fill="none" stroke="#fff" stroke-width="0.7"/></svg>
        www.pebblesmiles.com
      </li>
    </ul>

    <address class="address">
      418 Maple Grove Lane, Suite G<br>
      Cedar Heights, Tokyo
    </address>
  </section>

  <section class="card card--back">
    <div class="brand"><span class="brand__dot"></span>Pebble Smiles</div>
  </section>
</main>
</body>
</html>
```